Logo and Business Card for Dental Office

We are opening a periodontal office (dental specialist for dental implants and gum diseases). It is a brand new state of the art facility with a focus on the most effective treatments for retaining natural teeth, or replacing teeth with implants when they must be lost. Strong emphasis on customer service and amenities for patient comfort. We are located just outside of Boston, MA.

Target Market(s)

potential adult patients, dentists in the community that will refer patients for specialized care

Industry/Entity Type

Dental

Requirements
Must have
• business name, address, phone number, website
Marcus T. Pellinger, DMD LLC
427 Corliss Street, Ste 305
Wayland, MA 01694
508-555-0172
508-555-0148 Fax
DrPellinger.example

the uploaded file has a rough version of what I'm looking for in the logo, I like the colors but it can be varies some.
Nice to have
• simple logo or symbol on business card, one possible idea I had was an abstract symbol of a screw or threads that might represent a dental implant, the attached file gives an idea of where to start.
Should not have
• I want a professional feel, no cartoons of teeth that appear childish, etc
The font should be easy to read with no curly/swirly shapes.

```html
<!DOCTYPE html>
<html lang="en">
<head>
<meta charset="utf-8">
<title>Pellinger Periodontics – Business Card</title>
<link href="https://fonts.googleapis.com/css2?family=Source+Sans+3:wght@400;600&display=swap" rel="stylesheet">
<style>
  :root {
    --backdrop: #2c2e30;
    --card: #ffffff;
    --ink: #4a4b4d;
    --ink-soft: #6b6c6e;
    --brand-red: #a4120f;
    --band-text: #f6e9e8;
    --shadow: rgba(0, 0, 0, 0.45);
  }
  * { box-sizing: border-box; margin: 0; padding: 0; }
  html, body {
    width: 1200px;
    height: 900px;
    overflow: hidden;
    background: var(--backdrop);
    font-family: "Source Sans 3", "Helvetica Neue", Arial, sans-serif;
  }
  .card {
    position: absolute;
    top: 297px;
    width: 426px;
    height: 263px;
    background: var(--card);
    box-shadow: 0 10px 30px var(--shadow);
    overflow: hidden;
  }
  .card--front { left: 155px; }
  .card--back { left: 615px; }

  .brand {
    position: absolute;
    display: flex;
    align-items: center;
    gap: 12px;
  }
  .brand__dot {
    width: 30px;
    height: 30px;
    border-radius: 50%;
    background: var(--brand-red);
    flex: none;
  }
  .brand__name {
    font-weight: 600;
    font-size: 24px;
    color: var(--ink);
    letter-spacing: 0.2px;
    white-space: nowrap;
  }
  .card--front .brand { left: 56px; top: 112px; }
  .card--back .brand { left: 104px; top: 52px; }
  .card--back .brand__name { font-size: 22px; }

  .holder {
    position: absolute;
    left: 40px;
    top: 143px;
    font-size: 15px;
    color: var(--ink);
  }
  .holder__name { font-weight: 600; }

  .contact-band {
    position: absolute;
    left: 0;
    top: 169px;
    width: 100%;
    height: 56px;
    background: var(--brand-red);
    color: var(--band-text);
    font-size: 11px;
    line-height: 17px;
    padding: 5px 0 0 40px;
  }
  .contact-band .sep { margin: 0 8px; opacity: 0.8; }
  .contact-band__mark {
    position: absolute;
    right: 28px;
    top: 14px;
    width: 26px;
    height: 26px;
    border-radius: 50%;
    background: rgba(255, 255, 255, 0.25);
  }
</style>
</head>
<body>
  <section class="card card--front" aria-label="Business card front">
    <div class="brand">
      <span class="brand__dot"></span>
      <span class="brand__name">Pellinger Periodontics</span>
    </div>
  </section>

  <section class="card card--back" aria-label="Business card back">
    <div class="brand">
      <span class="brand__dot"></span>
      <span class="brand__name">Pellinger Periodontics</span>
    </div>
    <p class="holder"><span class="holder__name">Marcus T. Pellinger</span>, DMD LLC</p>
    <div class="contact-band">
      <p>A. 427 Corliss Street, Ste 305 Carrow Falls, ME 01694</p>
      <p>P. 508-555-0172<span class="sep">|</span>F. 508-555-0148</p>
      <p>W. DrPellinger.example</p>
      <span class="contact-band__mark"></span>
    </div>
  </section>
</body>
</html>
```